依頼概要
■依頼の目的/概要
「かざみ百選名店の会」は足利市内の26の店舗がそれぞれの良い所を伸ばそうとする「逸品運動」を中心に共同で事業を行う組織です。
栃木県足利市は国宝澄柾寺、日本遺産蓮沼学舎などの重要な史跡が点在すところから東の京都、北の鎌倉などと言われることがあります。また、霧浦橋、ミモザランド、岸辺ゆうたの故郷など観光などのポイントが多数あります。
※添付ファイルに会員のカタログがあります。

■依頼詳細
「かざみ百選名店の会」加盟の店舗は市内の各所に点在しております。そのためそれぞれの店舗の店頭に飾れるような「のぼり旗」のデザインを募集します。
※添付ファイルに地図があります。

■重視する点
【必須項目】
「かざみ百選名店の会」という文字表記

のぼり旗という制約のあるデザインの中で名店会らしさ、足利らしさなどを取り込んだものを希望します。通常ののぼり旗の概念を逸脱するものでも結構ですが、予算が必要以上にかかり様なアイデアは採用が難しくなる可能性がございます。

その他何かご不明な点がございましたら、お気軽にご質問下さい。
よろしくお願いいたします。
足利市のイメージキャラクターをのぼりデザインに使用する事は可能です。
ただし「かざみ百選名店会」のイメージキャラクターではございませんのでご確認ください。
なお、キャラクター使用許諾につきましては当会にて行います。
添付データとして「ころまる君」のイラストレータデータを添付させていただきますのでこちらを使用願います。
(※当依頼以外でころまる君の画像当を使用する場合は瀬尾野観光協会の許可が必要ですのでご注意ください。)
百選名店の会全体会議にてデザインの選定を行う予定です。
そのため直前の3月14日まで受付を延長させていただきます。
より多くの提案をお願いしたいと思います。

百選名店の会の会員からのアンケート調査に基づいて決定いたしました。

このたびは名店会ののぼりをデザイン頂き誠にありがとうございます。
市内の各所にこのデザインが掲載されお客様に親しまれるように頑張りたいと思います。

```html
<!DOCTYPE html>
<html lang="ja">
<head>
<meta charset="utf-8">
<title>かざみ百選名店の会 のぼり旗</title>
<link href="https://fonts.googleapis.com/css2?family=M+PLUS+Rounded+1c:wght@500;800;900&display=swap" rel="stylesheet">
<style>
  :root {
    --page: #ffffff;
    --ink: #1a1a1a;
    --magenta: #d6177f;
    --magenta-deep: #b0106a;
    --lime: #d9e84a;
    --pink-soft: #f7b8d8;
    --yellow-soft: #f3ef6a;
    --green-soft: #9fd86a;
    --orange-soft: #f7b25a;
    --teal-soft: #6fd0c8;
    --panel: #ffffff;
  }
  html, body {
    margin: 0;
    padding: 0;
    width: 1200px;
    height: 2219px;
    overflow: hidden;
    background: var(--page);
  }
  .canvas {
    position: relative;
    width: 1200px;
    height: 2219px;
    font-family: "M PLUS Rounded 1c", sans-serif;
  }
  .banner {
    position: absolute;
    left: 268px;
    top: 152px;
    width: 660px;
    height: 1895px;
    background: var(--page);
    outline: 2px solid #d8d8d8;
    overflow: hidden;
  }
  .banner-header {
    position: absolute;
    left: 0; top: 0;
    width: 100%;
    height: 240px;
    display: flex;
    align-items: center;
    justify-content: center;
  }
  .tagline {
    margin: 0;
    font-weight: 900;
    font-size: 64px;
    letter-spacing: 2px;
    color: var(--ink);
  }
  .pattern-field {
    position: absolute;
    left: 0; top: 240px;
    width: 100%;
    height: 1655px;
    background:
      radial-gradient(circle at 15% 10%, var(--orange-soft) 0 12%, transparent 22%),
      radial-gradient(circle at 85% 8%, var(--green-soft) 0 10%, transparent 20%),
      radial-gradient(circle at 10% 45%, var(--teal-soft) 0 9%, transparent 18%),
      radial-gradient(circle at 90% 50%, var(--yellow-soft) 0 12%, transparent 22%),
      radial-gradient(circle at 12% 85%, var(--yellow-soft) 0 12%, transparent 22%),
      radial-gradient(circle at 88% 90%, var(--orange-soft) 0 10%, transparent 20%),
      linear-gradient(180deg, var(--pink-soft), #fbd6ea 50%, var(--pink-soft));
  }
  .panel {
    position: absolute;
    left: 150px;
    top: 300px;
    width: 400px;
    height: 1450px;
    background: var(--panel);
    border-radius: 200px;
  }
  .club-prefix {
    position: absolute;
    left: 250px;
    top: 370px;
    margin: 0;
    font-weight: 900;
    font-size: 96px;
    line-height: 1;
    color: var(--magenta);
    -webkit-text-stroke: 5px var(--lime);
    paint-order: stroke fill;
  }
  .vertical {
    position: absolute;
    margin: 0;
    display: flex;
    flex-direction: column;
    align-items: center;
  }
  .vertical span {
    display: block;
    text-align: center;
  }
  .vertical .turn {
    transform: rotate(90deg);
  }
  .club-name {
    left: 318px;
    top: 500px;
    width: 190px;
    font-weight: 900;
    font-size: 170px;
    line-height: 176px;
    color: var(--magenta);
    -webkit-text-stroke: 7px var(--lime);
    paint-order: stroke fill;
  }
  .club-about {
    left: 222px;
    top: 500px;
    width: 34px;
    font-weight: 800;
    font-size: 27px;
    line-height: 29px;
    color: var(--magenta-deep);
  }
  .member-label {
    position: absolute;
    left: 340px;
    top: 1580px;
    margin: 0;
    font-weight: 900;
    font-size: 52px;
    line-height: 1;
    color: var(--ink);
  }
</style>
</head>
<body>
<main class="canvas">
  <section class="banner">
    <header class="banner-header">
      <p class="tagline">素敵がいっぱい!!</p>
    </header>
    <div class="pattern-field" role="img" aria-label="カラフルな蝶の模様が一面に広がる背景"></div>
    <div class="panel"></div>
    <p class="club-prefix">かざみ</p>
    <h1 class="vertical club-name" aria-label="百選名店の会">
      <span>百</span><span>選</span><span>名</span><span>店</span><span>の</span><span>会</span>
    </h1>
    <p class="vertical club-about" aria-label="かざみ百選名店の会＝すぐれた品・サービス・技術のお店を紹介する団体です。">
      <span>か</span><span>ざ</span><span>み</span><span>百</span><span>選</span><span>名</span><span>店</span><span>の</span><span>会</span><span class="turn">＝</span><span>す</span><span>ぐ</span><span>れ</span><span>た</span><span>品</span><span>・</span><span>サ</span><span class="turn">ー</span><span>ビ</span><span>ス</span><span>・</span><span>技</span><span>術</span><span>の</span><span>お</span><span>店</span><span>を</span><span>紹</span><span>介</span><span>す</span><span>る</span><span>団</span><span>体</span><span>で</span><span>す</span><span>。</span>
    </p>
    <p class="member-label">加盟店</p>
  </section>
</main>
</body>
</html>
```